Comprehensive Branding Development for Brightvale Holdings Limited

We have our logo and are seeking a talented graphic designer to help us develop a cohesive branding guideline based on this logo provided by our client.
The goal is to create a comprehensive branding package for various office stationery items and promotional materials.

Deliverables:

The designer will be responsible for creating branding guidelines for the following items:

Letterhead
Envelope
Business card
Key holders
T-shirts
Face cap
Car branding
Pen
Dangler (Air Fresheners)
Lapel pin
PowerPoint template
ID card
Carrier bag
Notebook
Mug cup
Umbrella

Logo Text

Logo Provided by client and no needs for designing a new logo

```html
<!DOCTYPE html>
<html lang="en">
<head>
<meta charset="utf-8">
<title>Brightvale Holdings Limited – Stationery and Vehicle Livery</title>
<link href="https://fonts.googleapis.com/css2?family=Open+Sans:wght@400;600&family=Roboto:ital,wght@1,700&display=swap" rel="stylesheet">
<style>
  :root{
    --brand-red:#e31e24;
    --brand-grey:#8a8a8c;
    --brand-light-grey:#c9c9cb;
    --ink:#111111;
    --paper:#ffffff;
    --stage:#ececec;
    --van-body:#f7f7f7;
  }
  *{box-sizing:border-box;margin:0;padding:0}
  html,body{width:962px;height:1200px;overflow:hidden}
  body{background:var(--stage);position:relative;font-family:"Open Sans",Arial,sans-serif;color:var(--brand-grey)}
  .item{position:absolute;overflow:hidden;box-shadow:0 2px 6px rgba(0,0,0,.12)}
  .wordmark{font-family:"Open Sans",Arial,sans-serif;font-weight:400;color:var(--brand-red);letter-spacing:.02em;text-transform:uppercase;display:flex;align-items:center;gap:6px;line-height:1.05}
  .wordmark .mark-square{display:inline-block;background:var(--brand-red);flex:none}
  .wordmark.on-dark{color:var(--paper)}
  .wordmark.on-dark .mark-square{background:var(--paper)}
  .contact{font-family:Roboto,Arial,sans-serif;font-style:italic;font-weight:700;color:var(--brand-grey)}
  .contact.on-dark{color:var(--paper)}
  .band{position:absolute;left:0;right:0}
  .band-red{background:var(--brand-red);color:var(--paper)}
  .band-grey{background:var(--brand-grey);color:var(--paper)}
  .band span{display:block;text-transform:uppercase;font-family:Roboto,Arial,sans-serif;font-style:italic;font-weight:700;white-space:nowrap}
  .stripe{position:absolute;transform:skewX(-35deg)}
  .stripe-red{background:var(--brand-red)}
  .stripe-grey{background:var(--brand-grey)}
  .stripe-pale-red{background:var(--brand-red);opacity:.12}
  .stripe-pale-grey{background:var(--brand-grey);opacity:.12}
  .reg-no{position:absolute;font-size:5px;color:var(--brand-grey)}

  /* Letterhead */
  .letterhead{left:592px;top:30px;width:340px;height:480px;background:var(--paper)}
  .letterhead .wordmark{position:absolute;left:24px;bottom:64px;font-size:14px}
  .letterhead .wordmark .mark-square{width:12px;height:12px}
  .letterhead .contact{position:absolute;left:24px;bottom:12px;font-size:8px}
  .letterhead .band-red{bottom:40px;height:10px;left:150px}
  .letterhead .band-grey{bottom:28px;height:9px;left:150px}
  .letterhead .band span{font-size:6.5px;padding:1px 0 0 8px}

  /* Folder */
  .folder{left:30px;top:40px;width:490px;height:220px;background:var(--ink)}

  /* Envelope */
  .envelope{left:30px;top:290px;width:490px;height:240px;background:var(--paper)}
  .envelope .flap{position:absolute;left:0;top:0}
  .envelope .wordmark{position:absolute;left:26px;top:126px;font-size:15px}
  .envelope .wordmark .mark-square{width:12px;height:12px}
  .envelope .contact{position:absolute;left:26px;top:152px;font-size:9.5px;line-height:1.45}
  .envelope .band-red{top:196px;height:12px;left:0}
  .envelope .band-grey{top:211px;height:10px;left:0}
  .envelope .band span{font-size:7px;padding:1px 0 0 26px}

  /* Business cards */
  .card{width:270px;height:160px}
  .card-front{left:30px;top:560px;background:var(--paper)}
  .card-back{left:320px;top:560px;background:var(--ink)}
  .card .wordmark{position:absolute;left:18px;top:28px;font-size:12px}
  .card .wordmark .mark-square{width:10px;height:10px}
  .card .contact{position:absolute;left:18px;top:78px;font-size:8.5px;line-height:1.5}
  .card-front .band-red{top:120px;height:10px}
  .card-front .band-grey{top:133px;height:9px}
  .card-front .band span{font-size:6px;padding:1px 0 0 18px}

  /* Ruler */
  .ruler{left:620px;top:560px;width:312px;height:64px;background:var(--brand-light-grey)}
  .ruler .scale{position:absolute;left:0;top:0}
  .ruler .wordmark{position:absolute;left:14px;bottom:8px;font-size:12px;color:var(--ink)}
  .ruler .wordmark .mark-square{width:9px;height:9px;background:var(--ink)}

  /* Vehicle livery */
  .livery{position:absolute;left:70px;top:780px;width:822px;height:370px}
  .van-body{position:absolute;inset:0;border-radius:60px 140px 40px 40px;background:var(--van-body);box-shadow:0 10px 24px rgba(0,0,0,.12);overflow:hidden}
  .van-window{position:absolute;left:500px;top:40px;width:200px;height:110px;border-radius:8px 70px 8px 8px;background:linear-gradient(135deg,#b9bfc3,#e3e6e8)}
  .van-wheel{position:absolute;bottom:-40px;width:130px;height:130px;border-radius:50%;background:radial-gradient(circle,#bdbdbd 0 28%,#222 30% 100%)}
  .van-wheel.rear{left:110px}
  .van-wheel.front{left:610px}
  .livery .wordmark{position:absolute;left:230px;top:70px;font-size:26px}
  .livery .wordmark .mark-square{width:20px;height:20px}
  .livery .contact{position:absolute;left:240px;top:186px;font-size:15px;line-height:1.55;display:flex;flex-direction:column}
  .icon{display:inline-block;vertical-align:-2px;margin-right:5px}
</style>
</head>
<body>

<section class="item letterhead" aria-label="Letterhead">
  <div class="stripe stripe-pale-red" style="left:140px;top:120px;width:40px;height:200px"></div>
  <div class="stripe stripe-pale-grey" style="left:200px;top:90px;width:50px;height:260px"></div>
  <div class="wordmark"><span class="mark-square"></span>Brightvale Holdings Limited</div>
  <div class="band band-red"><span>Unlocking opportunities</span></div>
  <div class="band band-grey"><span>Asset management &nbsp;•&nbsp; Wealth management</span></div>
  <div class="contact">+234 800-555-0142 &nbsp;&nbsp; brightvaleholdings.com</div>
  <div class="reg-no" style="right:10px;bottom:54px">RC 000000</div>
</section>

<section class="item folder" aria-label="Presentation folder">
  <div class="stripe stripe-red" style="left:10px;top:0;width:40px;height:220px"></div>
  <div class="stripe stripe-grey" style="left:90px;top:0;width:60px;height:220px"></div>
  <div class="stripe stripe-red" style="left:200px;top:110px;width:50px;height:110px"></div>
</section>

<section class="item envelope" aria-label="DL envelope">
  <svg class="flap" width="490" height="120" viewBox="0 0 490 120" aria-hidden="true">
    <polyline points="0,0 245,110 490,0" fill="none" stroke="#e2e2e2" stroke-width="2"/>
  </svg>
  <div class="stripe stripe-red" style="left:330px;top:0;width:36px;height:110px"></div>
  <div class="stripe stripe-grey" style="left:400px;top:0;width:50px;height:190px"></div>
  <div class="wordmark"><span class="mark-square"></span>Brightvale Holdings Limited</div>
  <div class="contact">
    <div><svg class="icon" width="9" height="9" viewBox="0 0 10 10" aria-hidden="true"><path d="M2 1l2 2-1 1.5a6 6 0 0 0 2.5 2.5L7 6l2 2-1.5 1.5C4 9 1 6 .5 2.5z" fill="var(--brand-red)"/></svg>+234 800-555-0142</div>
    <div><svg class="icon" width="9" height="9" viewBox="0 0 10 10" aria-hidden="true"><circle cx="5" cy="5" r="4.2" fill="none" stroke="var(--brand-red)" stroke-width="1.2"/><line x1="1" y1="5" x2="9" y2="5" stroke="var(--brand-red)"/></svg>brightvaleholdings.com</div>
  </div>
  <div class="band band-red"><span>Unlocking opportunities</span></div>
  <div class="band band-grey"><span>Asset management &nbsp;•&nbsp; Wealth management</span></div>
  <div class="reg-no" style="right:14px;top:186px">RC 000000</div>
</section>

<section class="item card card-front" aria-label="Business card front">
  <div class="stripe stripe-pale-red" style="left:190px;top:0;width:22px;height:70px"></div>
  <div class="stripe stripe-pale-grey" style="left:225px;top:0;width:30px;height:110px"></div>
  <div class="wordmark"><span class="mark-square"></span>Brightvale Holdings Limited</div>
  <div class="contact">
    <div>+234 800-555-0142</div>
    <div>brightvaleholdings.com</div>
  </div>
  <div class="band band-red"><span>Unlocking opportunities</span></div>
  <div class="band band-grey"><span>Asset management &nbsp;•&nbsp; Wealth management</span></div>
</section>

<section class="item card card-back" aria-label="Business card back">
  <div class="wordmark on-dark"><span class="mark-square"></span>Brightvale Holdings Limited</div>
  <div class="contact on-dark" style="left:140px;top:70px">
    <div>+234 800-555-0142</div>
    <div>brightvaleholdings.com</div>
  </div>
  <div class="stripe stripe-red" style="left:0;top:80px;width:22px;height:80px"></div>
  <div class="stripe stripe-grey" style="left:50px;top:70px;width:30px;height:90px"></div>
  <div class="stripe stripe-red" style="left:100px;top:120px;width:26px;height:40px"></div>
</section>

<section class="item ruler" aria-label="Ruler">
  <svg class="scale" width="312" height="20" viewBox="0 0 312 20" aria-hidden="true">
    <path d="M10 0v10M22 0v6M34 0v10M46 0v6M58 0v10M70 0v6M82 0v10M94 0v6M106 0v10M118 0v6M130 0v10M142 0v6M154 0v10M166 0v6M178 0v10M190 0v6M202 0v10M214 0v6M226 0v10M238 0v6M250 0v10M262 0v6M274 0v10M286 0v6M298 0v10" stroke="#6d6d6f" stroke-width="1"/>
  </svg>
  <div class="wordmark"><span class="mark-square"></span>Brightvale Holdings Limited</div>
</section>

<section class="livery" aria-label="Vehicle side livery">
  <div class="van-body" role="img" aria-label="Side view of a white compact van carrying the brand livery">
    <div class="stripe stripe-red" style="left:10px;top:0;width:60px;height:110px"></div>
    <div class="stripe stripe-grey" style="left:110px;top:0;width:70px;height:300px"></div>
    <div class="stripe stripe-red" style="left:130px;top:150px;width:60px;height:150px"></div>
    <div class="van-window"></div>
  </div>
  <div class="van-wheel rear" aria-hidden="true"></div>
  <div class="van-wheel front" aria-hidden="true"></div>
  <div class="wordmark"><span class="mark-square"></span>Brightvale Holdings Limited</div>
  <div class="contact">
    <span><svg class="icon" width="13" height="13" viewBox="0 0 10 10" aria-hidden="true"><path d="M2 1l2 2-1 1.5a6 6 0 0 0 2.5 2.5L7 6l2 2-1.5 1.5C4 9 1 6 .5 2.5z" fill="var(--brand-red)"/></svg>+234 800-555-0142</span>
    <span><svg class="icon" width="13" height="13" viewBox="0 0 10 10" aria-hidden="true"><circle cx="5" cy="5" r="4.2" fill="none" stroke="var(--brand-red)" stroke-width="1.2"/><line x1="1" y1="5" x2="9" y2="5" stroke="var(--brand-red)"/></svg>brightvaleholdings.com</span>
  </div>
</section>

</body>
</html>
```